Mortgage Loan officer needs clean/modern business card design

Looking for a clean, modern 2-sided business card design. We like the earth tones used in our logo and website http://vukarhome-lending.example . Would also like to incorporate: 1) Something special to make our card stand out - a pop of color or embossed logo, for instance and 2) please include "Mortgage Loans" "Reverse Mortgages" "Private Money Loans" on back of card with the logo.

Front: Needs to include agent/company license info - see website. Agent name: Niall Hargrove

Here are fonts and colors used for our logo:
Font: Avenir Next
Colors:
#2c3539 - Dark Gray
#576870 - Light Gray
#ffffff - Background White

Target Market(s)

Prospects and current clients. Will also be distributing to people in professional network (attorneys and CPAs)

Industry/Entity Type

Business

Contact Information for Business Card

Include agent name, contact info, website on front, licensing info for agent an company. Logo and services offered on back

Font styles to use
Other font styles liked:
• Avenir Next

Requirements
Must have
• See project description
Should not have
• Nothing cheesy

```html
<!DOCTYPE html>
<html lang="en">
<head>
<meta charset="utf-8">
<title>Niall Hargrove – Business Card</title>
<link rel="stylesheet" href="https://fonts.googleapis.com/css2?family=Nunito+Sans:wght@400;700;800&display=swap">
<style>
  :root{
    --dark-gray:#2c3539;
    --light-gray:#576870;
    --white:#ffffff;
    --page:#eceeef;
    --panel-dark:#3a3b3c;
    --panel-mid:#4a4b4c;
    --panel-deep:#2f3031;
    --divider:#9aa3a7;
  }
  *{box-sizing:border-box;margin:0;padding:0}
  html,body{width:1187px;height:1200px;overflow:hidden}
  body{background:var(--page);font-family:"Nunito Sans",sans-serif;color:var(--dark-gray);position:relative}

  .card{position:absolute;left:143px;width:900px;height:544px;box-shadow:0 2px 8px rgba(0,0,0,.18)}
  .card-back{top:40px}
  .card-front{top:634px;background:var(--white);border:1px solid #c9cdcf}

  /* back side */
  .panel-texture{position:absolute;inset:0;
    background:
      repeating-linear-gradient(90deg,rgba(0,0,0,.18) 0 2px,transparent 2px 80px),
      linear-gradient(90deg,var(--panel-deep),var(--panel-mid) 35%,var(--panel-dark) 70%,var(--panel-deep));}
  .brand-disc{position:absolute;left:100px;top:125px;width:288px;height:288px;border-radius:50%;background:var(--white);
    display:flex;align-items:center;justify-content:center;text-align:center}
  .brand-name{font-size:30px;font-weight:400;line-height:1.2;color:var(--dark-gray)}
  .back-divider{position:absolute;left:447px;top:188px;height:181px;border-left:2px dotted var(--divider)}
  .services{position:absolute;left:484px;top:200px;list-style:none}
  .services li{display:flex;align-items:center;height:60px;color:var(--white);font-weight:800;font-size:25px;letter-spacing:1.2px}
  .services svg{width:32px;height:32px;margin-right:14px;flex:none}

  /* front side */
  .agent-name{position:absolute;top:56px;width:100%;text-align:center;font-size:43px;font-weight:800;color:var(--dark-gray)}
  .agent-title{position:absolute;top:110px;width:100%;text-align:center;font-size:27px;color:var(--light-gray);letter-spacing:.5px}
  .contact-col{position:absolute;top:188px;list-style:none}
  .contact-col li{display:flex;align-items:center;height:60px;font-size:23px;color:var(--dark-gray);line-height:1.1;white-space:nowrap}
  .contact-col svg{width:30px;height:30px;flex:none;margin-right:12px;stroke:var(--light-gray);fill:none;stroke-width:1.6}
  .col-left{left:62px;width:370px}
  .col-right{left:478px}
  .front-divider{position:absolute;left:455px;top:179px;height:181px;border-left:2px dotted var(--divider)}
  .license{position:absolute;top:414px;width:100%;text-align:center;font-size:25px;line-height:34px;color:var(--dark-gray)}
</style>
</head>
<body>

<section class="card card-back" aria-label="Card back">
  <div class="panel-texture" role="img" aria-label="Dark charcoal vertical wood-plank texture"></div>
  <div class="brand-disc"><span class="brand-name">The Hargrove<br>Group</span></div>
  <div class="back-divider"></div>
  <ul class="services">
    <li><svg viewBox="0 0 32 32"><circle cx="16" cy="16" r="13" fill="none" stroke="#fff" stroke-width="2.5"/><path d="M10 16.5l4 4 8-8.5" fill="none" stroke="#fff" stroke-width="3" stroke-linecap="round" stroke-linejoin="round"/></svg>Mortgage Loans</li>
    <li><svg viewBox="0 0 32 32"><circle cx="16" cy="16" r="13" fill="none" stroke="#fff" stroke-width="2.5"/><path d="M10 16.5l4 4 8-8.5" fill="none" stroke="#fff" stroke-width="3" stroke-linecap="round" stroke-linejoin="round"/></svg>Reverse Mortgages</li>
    <li><svg viewBox="0 0 32 32"><circle cx="16" cy="16" r="13" fill="none" stroke="#fff" stroke-width="2.5"/><path d="M10 16.5l4 4 8-8.5" fill="none" stroke="#fff" stroke-width="3" stroke-linecap="round" stroke-linejoin="round"/></svg>Private Money Loans</li>
  </ul>
</section>

<section class="card card-front" aria-label="Card front">
  <h1 class="agent-name">Niall Hargrove</h1>
  <p class="agent-title">LOAN OFFICER</p>

  <ul class="contact-col col-left">
    <li><svg viewBox="0 0 32 32"><rect x="10" y="3" width="12" height="26" rx="2"/><line x1="14" y1="25" x2="18" y2="25"/></svg>+ 650 2740 318 902</li>
    <li><svg viewBox="0 0 32 32"><rect x="3" y="8" width="26" height="17"/><path d="M3 8l13 10 13-10M3 25l10-9M29 25l-10-9"/></svg>hello@vukarhome.example</li>
    <li><svg viewBox="0 0 32 32"><circle cx="16" cy="16" r="12"/><ellipse cx="16" cy="16" rx="5" ry="12"/><path d="M4 16h24M6 10h20M6 22h20"/></svg>vukarhome-lending.example</li>
  </ul>

  <div class="front-divider"></div>

  <ul class="contact-col col-right">
    <li><svg viewBox="0 0 32 32"><path d="M7 4l5 0 2 6-3 2c1.5 4 4.5 7 9 9l2-3 6 2v5c0 1-1 2-2 2C14 27 5 18 5 6c0-1 1-2 2-2z"/></svg>+ 408-555-0172 x214</li>
    <li><svg viewBox="0 0 32 32"><path d="M16 29s-9-10-9-16a9 9 0 0118 0c0 6-9 16-9 16z"/><circle cx="16" cy="13" r="3.5"/></svg>Hearthline Lending</li>
    <li><svg viewBox="0 0 32 32"><path d="M3 15L16 6l13 9z" fill="#576870"/><rect x="6" y="15" width="20" height="11"/></svg>2280 Willow Crest, Suite<br>305, Campbell, CA 95008</li>
  </ul>

  <p class="license">Fed and State License<br>NMLS:417203 DRE:02286419 CO: DRE:01937562/NMLS:508817</p>
</section>

</body>
</html>
```